Inspiration Poster

Inspirational Poster that has a Kamran Dulo like abstract look (http://www.vexalo.com/images/search?q=kamran+dulo&FORM=HDRSC2) with the text:

"we walk not in order to arrive at the promise land but because walking itself is a revolution"
-Peter Ambrick

```html
<!DOCTYPE html>
<html lang="en">
<head>
<meta charset="utf-8">
<title>Inspiration Poster — Peter Ambrick</title>
<link rel="stylesheet" href="https://fonts.googleapis.com/css2?family=Montserrat:wght@300;700&display=swap">
<style>
  :root {
    --poster-black: #000000;
    --ink-white: #ffffff;
    --art-tone: #161616;
  }
  * { margin: 0; padding: 0; box-sizing: border-box; }
  html, body {
    width: 999px;
    height: 1200px;
    overflow: hidden;
    background: var(--poster-black);
  }
  .poster {
    position: relative;
    width: 999px;
    height: 1200px;
    background: var(--poster-black);
    color: var(--ink-white);
    font-family: "Montserrat", sans-serif;
  }
  .walking-art {
    position: absolute;
    left: 287px;
    top: 0;
    width: 372px;
    height: 279px;
  }
  .quote {
    position: absolute;
    left: 98px;
    top: 372px;
    font-size: 64px;
    line-height: 73px;
    font-weight: 300;
    letter-spacing: 1px;
    text-transform: uppercase;
  }
  .quote strong { font-weight: 700; }
  .quote .line { display: block; white-space: nowrap; }
  .author {
    position: absolute;
    left: 98px;
    top: 1011px;
    font-size: 64px;
    line-height: 73px;
    font-weight: 300;
    letter-spacing: 1px;
    text-transform: uppercase;
  }
  .author strong { font-weight: 700; }
</style>
</head>
<body>
  <main class="poster">
    <svg class="walking-art" role="img" aria-label="White line illustration of two legs in trousers and shoes mid-stride" viewBox="0 0 372 279">
      <rect width="372" height="279" fill="var(--art-tone)"/>
    </svg>

    <p class="quote">
      <span class="line">We <strong>walk</strong></span>
      <span class="line">not in <strong>order</strong></span>
      <span class="line">to <strong>arrive</strong> at</span>
      <span class="line">the <strong>promise</strong></span>
      <span class="line">land but <strong>because</strong></span>
      <span class="line"><strong>walking</strong> itself</span>
      <span class="line">is a <strong>revolution.</strong></span>
    </p>

    <p class="author">Peter <strong>Ambrick</strong></p>
  </main>
</body>
</html>
```